Looking for a new business card design

We are looking for a corporate looking yet still a bit different then the rest. I would like the card black with the picture on the back and the phrase "Guiding every crew home safe" on the back as well. Then a clean look on the front with a bit of an edge.

Target Market(s)

Corporate oil executives and drilling supervisors

Industry/Entity Type

Oil And Gas

Contact Information for Business Card

Black, bold, clean lines.

Font styles to use
Sans Serif

Requirements
Must have
• Picture on the back with the slogan "Guiding every crew home safe"
• Black background
• Stands out

```html
<!DOCTYPE html>
<html lang="en">
<head>
<meta charset="utf-8">
<title>Halvard Field Services – Business Card</title>
<link href="https://fonts.googleapis.com/css2?family=Open+Sans:wght@400;600;700&display=swap" rel="stylesheet">
<style>
  :root{
    --stage:#3b3c3b;
    --card:#151617;
    --lime:#c9d41f;
    --blue:#3f6ea3;
    --white:#f4f4f4;
    --photo-dark:#101512;
    --photo-mid:#6d6548;
    --photo-light:#d9d6c4;
  }
  *{margin:0;padding:0;box-sizing:border-box}
  html,body{width:1200px;height:900px;overflow:hidden;background:var(--stage)}
  body{font-family:"Open Sans",Arial,sans-serif;position:relative}
  .card{position:absolute;left:285px;width:630px;height:360px;background:var(--card);overflow:hidden;box-shadow:0 10px 30px rgba(0,0,0,.45)}
  .card--back{top:60px}
  .card--front{top:480px}

  /* shared brand lockup */
  .brand{position:absolute;display:flex;align-items:center;gap:14px}
  .brand-dot{flex:none;width:48px;height:48px;border-radius:50%;background:var(--lime)}
  .brand-name{color:var(--lime);font-weight:700;font-size:24px;line-height:1.1}

  /* back */
  .site-photo{position:absolute;inset:0 0 44px 0;
    background:radial-gradient(ellipse at 48% 55%,var(--photo-light) 0%,var(--photo-mid) 38%,var(--photo-dark) 78%)}
  .brand--back{left:200px;top:120px}
  .slogan-band{position:absolute;left:0;right:0;bottom:0;height:44px;background:#050505;display:flex;align-items:center;justify-content:center}
  .slogan{color:var(--white);font-size:16px;letter-spacing:1.5px;font-weight:600}

  /* front */
  .brand--front{left:40px;top:78px}
  .contact{position:absolute;right:52px;top:100px;text-align:right;color:var(--white)}
  .contact__name{color:var(--lime);font-size:22px;font-weight:600;line-height:1.3}
  .contact__title{font-size:15px;margin-bottom:12px}
  .contact__address{font-size:14px;line-height:1.35;margin-bottom:12px}
  .contact__row{display:flex;justify-content:flex-end;align-items:center;gap:10px;font-size:14px;line-height:1.6}
  .contact__row svg{flex:none;width:16px;height:16px;fill:var(--lime)}
  .contact__row svg.icon-globe{fill:none;stroke:var(--lime);stroke-width:2}
  .edge-bar{position:absolute;right:0;top:70px;width:14px;height:220px;background:var(--blue)}
</style>
</head>
<body>

<section class="card card--back">
  <div class="site-photo" role="img" aria-label="Aerial night photograph of a lit drilling rig site"></div>
  <div class="brand brand--back">
    <span class="brand-dot"></span>
    <span class="brand-name">Halvard<br>Field Services Corp.</span>
  </div>
  <div class="slogan-band"><p class="slogan">Guiding every crew home safe</p></div>
</section>

<section class="card card--front">
  <div class="brand brand--front">
    <span class="brand-dot"></span>
    <span class="brand-name">Halvard<br>Field Services Corp.</span>
  </div>
  <div class="contact">
    <p class="contact__name">Marcus Lindell</p>
    <p class="contact__title">Manager</p>
    <p class="contact__address">1480 Ridge Way<br>Dalton TX 75010</p>
    <p class="contact__row">(780) 555-0147
      <svg viewBox="0 0 24 24"><path d="M6.6 10.8a15 15 0 006.6 6.6l2.2-2.2a1 1 0 011-.25 11 11 0 003.6.6 1 1 0 011 1V20a1 1 0 01-1 1A17 17 0 013 4a1 1 0 011-1h3.5a1 1 0 011 1 11 11 0 00.6 3.6 1 1 0 01-.25 1z"/></svg></p>
    <p class="contact__row">(403) 555-0193
      <svg viewBox="0 0 24 24"><path d="M6 3h12v5H6zM4 9h16a2 2 0 012 2v6h-4v4H6v-4H2v-6a2 2 0 012-2zm4 7v3h8v-3z"/></svg></p>
    <p class="contact__row">info@halvardfield.ca
      <svg viewBox="0 0 24 24"><path d="M2 5h20v14H2zm2 2v.4l8 5.3 8-5.3V7z"/></svg></p>
    <p class="contact__row">www.halvardfield.ca
      <svg class="icon-globe" viewBox="0 0 24 24"><circle cx="12" cy="12" r="9"/><ellipse cx="12" cy="12" rx="4" ry="9"/><path d="M3 12h18"/></svg></p>
  </div>
  <div class="edge-bar"></div>
</section>

</body>
</html>
```